Meridian Callware business card design

I would like to see some designs for a business card for Meridian Callware. I would like the business card to be double sided. It will need to have a similar colour / look and feel to our website www.meridiancallware.com.au I have also attached our latest flyer. Final designs to be handed over in Photoshop format so that I can edit the business card when needed please.

Industry/Entity Type

Business

Contact Information for Business Card

Kelvin Ashworth
sales@meridiancallware.com.au
Business Development Manager
ph: (08) 6517 2984
www.meridiancallware.com.au

Font styles to use
Serif
Sans Serif

Requirements
Must have
• If you could please utilise our colour scheme as seen on our website and the attached flyer.
• I would also like the final design to be in a Photoshop format so that I can edit it when needed please.

```html
<!DOCTYPE html>
<html lang="en">
<head>
<meta charset="utf-8">
<title>Meridian Callware – Business Card</title>
<link rel="stylesheet" href="https://fonts.googleapis.com/css2?family=Arimo:wght@400&family=Montserrat:wght@500&display=swap">
<style>
  :root {
    --page-bg: #b9b9b9;
    --card-white: #ffffff;
    --brand-blue: #0a7bbd;
    --ink-dark: #333335;
    --ink-black: #111111;
  }
  * { box-sizing: border-box; margin: 0; padding: 0; }
  html, body {
    width: 992px;
    height: 1200px;
    overflow: hidden;
    background: var(--page-bg);
  }
  .card {
    position: absolute;
    left: 99px;
    width: 807px;
    height: 461px;
    overflow: hidden;
  }
  .card-front { top: 104px; background: var(--card-white); }
  .card-back { top: 623px; background: var(--brand-blue); }

  .wordmark {
    font-family: "Montserrat", Arial, sans-serif;
    font-weight: 500;
    font-size: 62px;
    letter-spacing: -0.5px;
    line-height: 1;
    white-space: nowrap;
  }
  .card-front .wordmark {
    position: absolute;
    left: 57px;
    top: 85px;
    color: var(--ink-dark);
  }
  .card-back .wordmark {
    position: absolute;
    left: 0;
    right: 0;
    top: 202px;
    text-align: center;
    color: var(--card-white);
  }

  .person {
    position: absolute;
    left: 57px;
    top: 193px;
    font-family: "Arimo", Arial, sans-serif;
  }
  .person-name {
    font-size: 30px;
    color: var(--brand-blue);
    line-height: 1.1;
  }
  .person-title {
    font-size: 20px;
    color: var(--ink-black);
    margin-top: 3px;
  }

  .contact-list {
    position: absolute;
    left: 58px;
    top: 290px;
    list-style: none;
    font-family: "Arimo", Arial, sans-serif;
    font-size: 21px;
    color: var(--ink-black);
  }
  .contact-list li {
    display: flex;
    align-items: center;
    height: 32.5px;
  }
  .contact-icon {
    width: 15px;
    height: 15px;
    margin-right: 16px;
    flex-shrink: 0;
  }

  .front-rule {
    position: absolute;
    left: 0;
    top: 404px;
    width: 100%;
    height: 7px;
    background: var(--ink-dark);
  }
  .front-band {
    position: absolute;
    left: 0;
    top: 411px;
    width: 100%;
    height: 50px;
    background: var(--brand-blue);
  }
</style>
</head>
<body>
  <section class="card card-front">
    <div class="wordmark">Meridian Callware</div>

    <div class="person">
      <div class="person-name">Kelvin Ashworth</div>
      <div class="person-title">Business Development Manager</div>
    </div>

    <ul class="contact-list">
      <li>
        <svg class="contact-icon" viewBox="0 0 15 15" aria-hidden="true">
          <rect width="15" height="15" fill="#0a7bbd"/>
          <path d="M4 3.5 L6 3.5 L6.6 5.6 L5.6 6.4 Q6.6 8.6 8.7 9.5 L9.5 8.5 L11.5 9.1 L11.5 11.2 Q6.5 11.4 3.8 5.5 Z" fill="#fff"/>
        </svg>
        <span>(08) 6517 2984</span>
      </li>
      <li>
        <svg class="contact-icon" viewBox="0 0 15 15" aria-hidden="true">
          <rect width="15" height="15" fill="#0a7bbd"/>
          <circle cx="7.5" cy="7.5" r="4.3" fill="none" stroke="#fff" stroke-width="1.2"/>
          <path d="M3.2 7.5 H11.8 M7.5 3.2 Q5.3 7.5 7.5 11.8 M7.5 3.2 Q9.7 7.5 7.5 11.8" fill="none" stroke="#fff" stroke-width="0.9"/>
        </svg>
        <span>www.meridiancallware.com.au</span>
      </li>
      <li>
        <svg class="contact-icon" viewBox="0 0 15 15" aria-hidden="true">
          <rect width="15" height="15" fill="#0a7bbd"/>
          <rect x="3" y="4.5" width="9" height="6.5" fill="#fff"/>
          <path d="M3 4.5 L7.5 8.2 L12 4.5" fill="none" stroke="#0a7bbd" stroke-width="1"/>
        </svg>
        <span>sales@meridiancallware.com.au</span>
      </li>
    </ul>

    <div class="front-rule"></div>
    <div class="front-band"></div>
  </section>

  <section class="card card-back">
    <div class="wordmark">Meridian Callware</div>
  </section>
</body>
</html>
```